Natural deodorant label

Natural clean deodorant line. Need modernize label which can be sized for both the regular and travel size deodorants. 2.75 x 3" and 1x2". Important to highlight no baking soda and its natural. Also has no aluminum, preservatives, nor chemicals. Its gender inclusive and safe for all ages. Please see website at www.lorvatique.com. will attach current label. Will need a label that i would be able to update with new scents as they come. Want a clean look.
Updates

Need extra days to review

Target Market(s)

the working mother/wife that lives a clean healthy life and pushes that for her family

Industry/Entity Type

health and beauty/deodorant/natural

Colors

Designer to choose colors to be used in the design.

Requirements
Must have
• No baking soda and gender inclusive on label. Clean look. Very little to no picture art.
Nice to have
• Potentially a different color representing the different scents. A brief description of the deodorant scent underneath the scent name. This can be found under the drop down menu titled valdora deodorant scents on the website www.lorvatique.com. Area on front label for a small barcode.
Should not have
• misspelled words; dark label

```html
<!DOCTYPE html>
<html lang="en">
<head>
<meta charset="UTF-8">
<title>Lorvatique Valdora Deodorant Label</title>
<link rel="stylesheet" href="https://fonts.googleapis.com/css2?family=Cinzel:wght@500&family=Crimson+Pro:wght@400;500;600&family=Parisienne&display=swap">
<style>
  :root {
    --backdrop: #f4f4f4;
    --label: #efefef;
    --ink: #2b2b2b;
    --band: #c4aaa3;
    --band-text: #ffffff;
    --mark: #3a3a3a;
  }
  * { margin: 0; padding: 0; box-sizing: border-box; }
  html, body {
    width: 1200px; height: 1200px; overflow: hidden;
    background: var(--backdrop);
  }
  .label {
    position: absolute;
    left: 325px; top: 50px;
    width: 550px; height: 1100px;
    background: var(--label);
    color: var(--ink);
    text-align: center;
    font-family: "Crimson Pro", Georgia, serif;
  }
  .brand-mark {
    position: absolute;
    top: 125px; left: 50%;
    width: 110px; height: 110px;
    margin-left: -55px;
  }
  .brand-name {
    position: absolute;
    top: 268px; left: 0; right: 0;
    font-family: "Cinzel", Georgia, serif;
    font-weight: 500;
    font-size: 52px;
    letter-spacing: 1px;
    color: var(--ink);
  }
  .product-name {
    position: absolute;
    top: 438px; left: 0; right: 0;
    font-weight: 600;
    font-size: 66px;
    letter-spacing: 2px;
  }
  .scent-name {
    position: absolute;
    top: 712px; left: 0; right: 0;
    font-family: "Parisienne", cursive;
    font-size: 46px;
  }
  .tagline-band {
    position: absolute;
    top: 808px; left: 14px; right: 14px;
    height: 50px;
    background: var(--band);
    color: var(--band-text);
    font-size: 36px;
    font-weight: 500;
    line-height: 50px;
    letter-spacing: 2px;
  }
  .claims {
    position: absolute;
    top: 884px; left: 0; right: 0;
    list-style: none;
    font-size: 20px;
    line-height: 26px;
    letter-spacing: 1.5px;
  }
  .net-weight {
    position: absolute;
    top: 1030px; left: 0; right: 0;
    font-size: 26px;
    font-weight: 500;
    letter-spacing: 1px;
  }
</style>
</head>
<body>
  <main class="label">
    <svg class="brand-mark" viewBox="0 0 96 96" aria-hidden="true">
      <circle cx="48" cy="48" r="40" fill="var(--mark)"/>
    </svg>
    <div class="brand-name">Lorvatique</div>
    <h1 class="product-name">VALDORA</h1>
    <div class="scent-name">Tropical Passion</div>
    <div class="tagline-band">NATURALLY REFRESHING</div>
    <ul class="claims">
      <li>NO ALUMINUM</li>
      <li>NO BAKING SODA, NO PARABENS</li>
      <li>NO SYNTHETIC INGREDIENTS</li>
      <li>CRUELTY FREE AND VEGAN</li>
      <li>GENDER INCLUSIVE, SAFE FOR ALL AGES</li>
    </ul>
    <div class="net-weight">NET.WT. 2.5 OZ (70G)</div>
  </main>
</body>
</html>
```